Update New Business Card - For Start Up

I need to update my business card, I have our old version for example. I would like to keep to the same colors and theme. We are a threat reporting and case management tool for corporations and educational institutions.

Target Market(s)

Corporate Security and Human Resources, School Administrators and Superintendents.

Industry/Entity Type

Physical Security and Technology.

Contact Information for Business Card

My Name, Founder/CEO, phone number 555-214-6082, Logo, Web...

Colors
0054AA
0677BA
7BADD7
CADEEF
E8F1F8

Requirements
Must have
• Something new and trendy.

```html
<!DOCTYPE html>
<html lang="en">
<head>
<meta charset="utf-8">
<title>Quorvane Business Card</title>
<link href="https://fonts.googleapis.com/css2?family=Montserrat:wght@400;500;600;700&display=swap" rel="stylesheet">
<style>
  :root {
    --stage: #3b3b3d;
    --brand-blue: #1f80d0;
    --brand-blue-deep: #0677ba;
    --brand-sky: #7badd7;
    --paper: #ffffff;
    --paper-tint: #f3f4f6;
    --paper-shade: #d9dde1;
    --title-tint: #cadeef;
  }
  * { box-sizing: border-box; margin: 0; padding: 0; }
  html, body { width: 900px; height: 1200px; overflow: hidden; }
  body {
    background: var(--stage);
    font-family: "Montserrat", Arial, sans-serif;
    position: relative;
  }
  .card {
    position: absolute;
    top: 324px;
    width: 285px;
    height: 516px;
    overflow: hidden;
  }
  .card--front { left: 99px; }
  .card--back { left: 516px; background: var(--brand-blue); }
  .card-surface { position: absolute; inset: 0; display: block; }

  .brand {
    position: absolute;
    left: 0; right: 0;
    display: flex;
    align-items: center;
    justify-content: center;
    gap: 8px;
    font-weight: 600;
    letter-spacing: 1.5px;
    white-space: nowrap;
  }
  .brand-dot { width: 26px; height: 26px; border-radius: 50%; flex: none; }
  .card--front .brand {
    top: 82px;
    color: var(--brand-blue);
    font-size: 26px;
  }
  .card--front .brand-dot { background: var(--brand-blue); }
  .card--back .brand {
    top: 242px;
    color: var(--paper);
    font-size: 25px;
  }
  .card--back .brand-dot { border: 4px solid var(--paper); }

  .holder {
    position: absolute;
    top: 274px; left: 0; right: 0;
    text-align: center;
    color: var(--paper);
  }
  .holder-name { font-size: 19px; font-weight: 600; letter-spacing: 0.5px; }
  .holder-title {
    margin-top: 3px;
    font-size: 7.5px; font-weight: 500; letter-spacing: 1px;
    color: var(--title-tint);
    text-transform: uppercase;
  }

  .contact-list {
    position: absolute;
    left: 50px; top: 362px;
    list-style: none;
    color: var(--paper);
    font-size: 10px;
    font-weight: 500;
  }
  .contact-item { display: flex; align-items: center; gap: 12px; }
  .contact-item + .contact-item { margin-top: 16px; }
  .contact-icon { width: 14px; height: 14px; flex: none; }
  .contact-lines { line-height: 17px; }
</style>
</head>
<body>

<section class="card card--front" aria-label="Business card front">
  <svg class="card-surface" viewBox="0 0 285 516" role="img" aria-label="Light grey upper panel and blue lower panel, each carrying a faint repeating pattern of round marks, divided by a wave">
    <rect width="285" height="516" fill="var(--brand-blue)"/>
    <path d="M0 0 H285 V190 C230 200 190 236 130 238 C80 240 40 226 0 230 Z" fill="var(--paper-shade)"/>
    <path d="M0 0 H285 V180 C230 190 190 226 130 228 C80 230 40 216 0 220 Z" fill="var(--paper-tint)"/>
  </svg>

  <div class="brand"><span class="brand-dot"></span><span class="brand-name">QUORVANE</span></div>

  <div class="holder">
    <p class="holder-name">DANA WHITFIELD</p>
    <p class="holder-title">Chief Executive Officer</p>
  </div>

  <ul class="contact-list">
    <li class="contact-item">
      <svg class="contact-icon" viewBox="0 0 16 16" aria-hidden="true"><path d="M4 1.5 6.3 4.6 5 6.2c.9 1.9 2.4 3.4 4.3 4.3l1.6-1.3L14 11.5 12.6 14C7 13.6 2.4 9 2 3.4Z" fill="var(--paper)"/></svg>
      <span class="contact-lines">888-899-3799<br>555-214-6082</span>
    </li>
    <li class="contact-item">
      <svg class="contact-icon" viewBox="0 0 16 16" aria-hidden="true"><rect x="1.5" y="3.5" width="13" height="9" fill="none" stroke="var(--paper)" stroke-width="1.4"/><path d="M1.5 3.5 8 9l6.5-5.5" fill="none" stroke="var(--paper)" stroke-width="1.4"/></svg>
      <span class="contact-lines">dana@quorvane.co</span>
    </li>
    <li class="contact-item">
      <svg class="contact-icon" viewBox="0 0 16 16" aria-hidden="true"><circle cx="8" cy="8" r="6.3" fill="none" stroke="var(--paper)" stroke-width="1.3"/><ellipse cx="8" cy="8" rx="2.7" ry="6.3" fill="none" stroke="var(--paper)" stroke-width="1.1"/><path d="M1.7 8h12.6" stroke="var(--paper)" stroke-width="1.1"/></svg>
      <span class="contact-lines">www.quorvane.com</span>
    </li>
  </ul>
</section>

<section class="card card--back" aria-label="Business card back">
  <svg class="card-surface" viewBox="0 0 285 516" role="img" aria-label="Blue panel with a faint repeating pattern of round marks">
    <rect width="285" height="516" fill="var(--brand-blue)"/>
  </svg>
  <div class="brand"><span class="brand-dot"></span><span class="brand-name">QUORVANE</span></div>
</section>

</body>
</html>
```